Brochure Design Project law firm

we require a print brochure for marketing. the information is contained on our website www.brindlecourt.com.au
we need to appeal to smash repairers who do third party claims. which means, where a person has had a car accident where it is not their fault they want their car fixed by the smash repairer who agrees to do the repairs and then claims the money from the insurer directly.

we will need a logo and business cards too.

Industry/Entity Type

Law Firm

Requirements
Must have
• pictures, law firm and smash repairer related.

```html
<!DOCTYPE html>
<html lang="en">
<head>
<meta charset="utf-8">
<title>Brindle Court – Brochure</title>
<link rel="stylesheet" href="https://fonts.googleapis.com/css2?family=Didact+Gothic&family=Quicksand:wght@400;500&family=Noto+Serif:wght@700&display=swap">
<style>
:root{
  --ink:#1b1b1b;
  --black:#050505;
  --red:#e01c1c;
  --red-dark:#8e0b0b;
  --grey:#9a9a9a;
  --paper:#ffffff;
  --photo-a:#d9dde2;
  --photo-b:#3b4654;
  --plate-a:#5a1d14;
  --plate-b:#2a1410;
}
*{margin:0;padding:0;box-sizing:border-box}
html,body{width:1200px;height:752px;overflow:hidden;background:var(--paper)}
body{position:relative;font-family:"Didact Gothic",sans-serif;color:var(--ink)}
.page{position:absolute;top:0;height:752px;background:var(--paper)}
.page--left{left:0;width:597px}
.page--right{left:600px;width:600px}
.fold{position:absolute;left:597px;top:0;width:3px;height:752px;background:#e6e6e6}

.section-tag{position:absolute;height:24px;padding-left:6px;font-family:"Quicksand",sans-serif;font-weight:500;font-size:17px;line-height:24px;color:var(--red-dark);text-transform:uppercase;background:linear-gradient(90deg,var(--red) 0,var(--red) 3%,#f56a6a 30%,rgba(255,255,255,0) 100%)}
.section-tag::before{content:"";position:absolute;left:0;top:0;width:5px;height:100%;background:var(--red)}

.copy p{font-size:10px;line-height:10.5px;letter-spacing:-0.15px;margin-bottom:8px}
.copy--info{position:absolute;left:88px;top:100px;width:490px}
.footnote{position:absolute;left:88px;top:298px;width:490px;font-size:10px;line-height:11px;letter-spacing:-0.15px}
.copy--case{position:absolute;left:263px;top:364px;width:300px}

.plate{position:absolute;left:48px;top:342px;width:163px;height:190px;border-radius:9px;background:radial-gradient(circle at 50% 40%,var(--plate-a),var(--plate-b) 75%)}

.contact{position:absolute;left:140px;top:573px;width:220px;text-align:center;font-size:10.4px;line-height:20px;font-style:normal}

.footer{position:absolute;bottom:0;height:24px;background:var(--black);color:var(--grey);font-size:10.4px;line-height:24px}
.page--left .footer{left:0;width:597px;padding-left:88px}
.page--right .footer{left:0;width:600px;padding-left:143px}

.masthead{position:absolute;left:0;top:0;width:600px;height:125px;background:var(--black)}
.mark{position:absolute;left:68px;top:15px;width:80px;height:80px;border-radius:50%;background:radial-gradient(circle at 50% 35%,#555,#111 70%);border:2px solid #c8c8c8}
.brand{position:absolute;right:20px;top:58px;color:#fff;font-family:"Quicksand",sans-serif;font-weight:400;font-size:38px;line-height:40px;letter-spacing:1px;text-transform:uppercase}
.tagline{position:absolute;right:20px;top:104px;color:var(--red);font-family:"Quicksand",sans-serif;font-size:12px;letter-spacing:1px}

.photo{position:absolute;left:0;top:125px;width:600px;height:380px;background:linear-gradient(135deg,var(--photo-a) 0%,#f2f3f5 35%,#8c96a3 65%,var(--photo-b) 100%)}
.photo-caption{position:absolute;left:0;top:484px;width:600px;height:19px;background:rgba(40,40,40,.55);color:#f1f1f1;font-family:"Noto Serif",serif;font-weight:700;font-size:10.6px;line-height:19px;text-align:center;text-transform:uppercase}
.rule{position:absolute;left:0;top:505px;width:600px;height:3px;background:var(--red)}

.col-title{position:absolute;top:522px;font-family:"Quicksand",sans-serif;font-size:19px;font-weight:400;text-transform:uppercase}
.col{position:absolute;top:548px;width:248px}
.col p{font-size:10px;line-height:10.5px;letter-spacing:-0.15px;margin-bottom:10px}
.col--about{left:48px}
.col--services{left:338px}
</style>
</head>
<body>
<section class="page page--left">
  <h2 class="section-tag" style="left:44px;top:62px;width:168px">Information</h2>
  <div class="copy copy--info">
    <p>Do you have customers who ask if they can have their car repaired by you because you are known for quality and experience?</p>
    <p>What do you do when a client tells you that their insurer is telling them to take their car to another smash repairer because your quote is too high?</p>
    <p>We have a solution for you!</p>
    <p>If you send the repair estimate to your clients insurer, your clients insurer will not approve the repairs unless your hourly rate is lower than other smash repairers in your local area. For this reason you will receive a lower hourly rate to such an extent that it may become unprofitable for you to run your business or complete the job. As a result you may lose the work.</p>
    <p>Let us work for you!</p>
    <p>We recovery money for a living. We threaten large insurance companies with the threat of litigation. We recover extremely good rates for our customers and pass on the savings. Try us today.</p>
    <p>We can complete a claim within 6 weeks or we give you a discount.*</p>
  </div>
  <p class="footnote">*Conditions Apply - Please speak to one of our team who will explain the process.</p>

  <h2 class="section-tag" style="left:228px;top:323px;width:180px">Recent Case Law</h2>
  <div class="plate" role="img" aria-label="Golden scales of justice on a dark red background"></div>
  <div class="copy copy--case">
    <p>We provide an educational service to help our clients know their rights. We constantly publish articles and information sheets to help you uncomplicate the law.</p>
    <p>We demand the best from our staff and obtain the best results for our clients.</p>
    <p>Quick turnaround of claims so you can keep your cash flow strong. Ask us how!</p>
  </div>

  <h2 class="section-tag" style="left:228px;top:525px;width:150px;padding-left:30px">Contact</h2>
  <address class="contact">
    Phone: 0400 318 552<br>
    Email: office@brindlecourt.com.au<br>
    Fax: 02 9011 4720<br>
    PO Box 4410 Market Square NSW 2002<br>
    118 Alder Lane, HAYMARKET NSW 2001
  </address>

  <footer class="footer">We are committed to a high level of excellence and will strive to obtain the best result.</footer>
</section>

<div class="fold"></div>

<section class="page page--right">
  <header class="masthead">
    <div class="mark"></div>
    <div class="brand">Brindle Court</div>
    <div class="tagline">THE RIGHT MOVE</div>
  </header>

  <div class="photo" role="img" aria-label="Business team in suits shaking hands across a meeting table"></div>
  <div class="photo-caption">We are committed to a high level of excellence and will strive to obtain the best result.</div>
  <div class="rule"></div>

  <h2 class="col-title" style="left:32px">About Us</h2>
  <div class="col col--about">
    <p>We focus on insurance claims for smash repairers in 3rd party claims. We fight the big insurers to ensure your rights are secured.</p>
    <p>We assist smash repairers to make more money, find more work and improve levels of customer service for their clients.</p>
    <p>We have state of the art systems and a team of dedicated professionals who will guide you every step of the way.</p>
  </div>

  <h2 class="col-title" style="left:317px">Services</h2>
  <div class="col col--services">
    <p>We focus on 3rd party recovery for motor vehicle property damage claims. We fast track your claim to ensure the fastest turn around time. Our Sydney head office is located in Alder Lane.</p>
    <p>We know how important a quick turn around in a claim is so you can do more repair work and keep your business going.</p>
    <p>We have state of the art systems and a team of dedicated professionals who will guide you every step of the way. We are small enough to ensure that you have personal service. We come to you.</p>
  </div>

  <footer class="footer">PHONE: 0400 318 552 ,EMAIL: office@brindlecourt.com.au ,Fax: 02 9011 4720</footer>
</section>
</body>
</html>
```